PLM - Business Card Design Project

We need a business card based on our logo
Updates

Hi I just upload logo file in AI format Thanks and regards

Target Market(s)

Bank, Big companies, Business owners

Industry/Entity Type

Business

Font styles to use
Sans Serif

```html
<!DOCTYPE html>
<html lang="en">
<head>
<meta charset="UTF-8">
<title>PLM – Business Card</title>
<link href="https://fonts.googleapis.com/css2?family=Exo+2:wght@400;500&display=swap" rel="stylesheet">
<style>
  :root {
    --page: #eef0f3;
    --paper: #ffffff;
    --navy: #173a63;
    --navy-deep: #112f55;
    --ink: #1d3557;
    --light: #ffffff;
    --muted: #d6dfeb;
  }
  html, body {
    margin: 0;
    width: 1200px;
    height: 864px;
    overflow: hidden;
    background: var(--page);
    font-family: "Exo 2", sans-serif;
  }
  .card {
    position: absolute;
    left: 100px;
    top: 146px;
    width: 1000px;
    height: 572px;
    display: flex;
    background: var(--paper);
    box-shadow: 0 10px 30px rgba(0,0,0,0.12);
  }
  .card-front {
    width: 450px;
    display: flex;
    align-items: center;
    justify-content: center;
  }
  .brand {
    display: flex;
    align-items: center;
    gap: 16px;
    color: var(--ink);
    font-size: 64px;
    font-weight: 500;
    letter-spacing: 3px;
    line-height: 1;
  }
  .brand-square {
    width: 40px;
    height: 40px;
    background: var(--ink);
  }
  .card-back {
    flex: 1;
    position: relative;
    background: linear-gradient(180deg, var(--navy) 0%, var(--navy-deep) 100%);
    color: var(--light);
    border-left: 3px solid var(--light);
    box-shadow: inset 2px 0 0 var(--navy-deep);
  }
  .holder {
    position: absolute;
    left: 90px;
    top: 120px;
  }
  .holder-name {
    font-size: 34px;
    font-weight: 500;
    letter-spacing: 0.5px;
  }
  .holder-role {
    margin-top: 4px;
    font-size: 15px;
    color: var(--muted);
  }
  .contacts {
    position: absolute;
    left: 60px;
    top: 262px;
    margin: 0;
    padding: 0;
    list-style: none;
  }
  .contacts li {
    display: flex;
    align-items: flex-start;
    gap: 18px;
    font-size: 21px;
    letter-spacing: 0.6px;
    margin-bottom: 16px;
    line-height: 1.2;
  }
  .contacts svg {
    width: 22px;
    height: 22px;
    flex: none;
    margin-top: 2px;
    fill: var(--light);
  }
</style>
</head>
<body>
  <div class="card">
    <section class="card-front">
      <div class="brand">
        <span class="brand-square" aria-hidden="true"></span>
        <span class="brand-name">PLM</span>
      </div>
    </section>
    <section class="card-back">
      <div class="holder">
        <div class="holder-name">Julien Marchand</div>
        <div class="holder-role">Director</div>
      </div>
      <ul class="contacts">
        <li>
          <svg viewBox="0 0 24 24" aria-hidden="true"><path d="M3 8c0-2 2-3 9-3s9 1 9 3v2h-5V8H8v2H3zM6 11h12l2 9H4zM12 13a3 3 0 1 0 0 6a3 3 0 0 0 0-6z"/></svg>
          <span>0012 3456 780</span>
        </li>
        <li>
          <svg viewBox="0 0 24 24" aria-hidden="true"><path d="M2 5h20v14H2zM4 7v.5l8 6 8-6V7zM4 10v7h16v-7l-8 6z"/></svg>
          <span>info@plmconseil.com</span>
        </li>
        <li>
          <svg viewBox="0 0 24 24" aria-hidden="true"><path d="M2 4h20v13H13v2h4v2H7v-2h4v-2H2zM4 6v9h16V6z"/></svg>
          <span>www.plmconseil.com</span>
        </li>
        <li>
          <svg viewBox="0 0 24 24" aria-hidden="true"><path d="M12 3l10 9h-3v9h-5v-6h-4v6H5v-9H2z"/></svg>
          <span>Harbor Office Suite 00<br>Rue Vernet, Lyon 00000</span>
        </li>
      </ul>
    </section>
  </div>
</body>
</html>
```